Cold brew coffee concept

Web site/logo for cold brew coffee served in a keg tap. Cold brew coffee is a natural energy beverage roasted with fair trade/organic beans. Based in New England. Think- Fresh, Natural, Organic, Pure, Mills, Brick, Wood. Fernhollow Coldbrew.

Target Market(s)

Individuals looking for energy drinks without added sugar or dairy. Coffee connoisseurs.

Industry/Entity Type

Trade

Logo Text

Fernhollow Coldbrew

Number of Pages Required

1 page

Font styles to use
Serif

```html
<!DOCTYPE html>
<html lang="en">
<head>
<meta charset="utf-8">
<title>Cold Brew Coffee</title>
<link rel="stylesheet" href="https://fonts.googleapis.com/css2?family=Great+Vibes&family=Josefin+Sans:wght@300&display=swap">
<style>
  :root {
    --roast: #4a3128;
    --bean: #5a3d32;
    --gold: #b5994a;
    --gold-soft: #c2a65a;
    --cream: #f4ecc8;
  }
  html, body {
    margin: 0;
    padding: 0;
    overflow: hidden;
    background: var(--roast);
  }
  .canvas {
    width: 1200px;
    height: 1200px;
    display: block;
    background: radial-gradient(circle at 50% 50%, #52372c 0%, var(--roast) 70%);
  }
  .label-body { fill: var(--gold); }
  .rule { fill: var(--cream); }
  .seal { fill: var(--bean); }
  .seal-ring { fill: none; stroke: var(--bean); stroke-width: 1.2; }
  .title-script {
    font-family: "Great Vibes", cursive;
    font-size: 66px;
    fill: var(--cream);
  }
  .title-line {
    font-family: "Josefin Sans", sans-serif;
    font-weight: 300;
    font-size: 44px;
    fill: var(--cream);
  }
  .icon-fill { fill: var(--bean); }
  .icon-stroke { fill: none; stroke: var(--bean); stroke-width: 6; stroke-linejoin: round; }
  .pattern-area { fill: var(--gold-soft); }
</style>
</head>
<body>
<svg class="canvas" viewBox="0 0 800 800" width="1200" height="1200" role="img" aria-label="Cold Brew Coffee label">
  <path class="label-body" d="M190,73 L570,73 L598,108 C660,120 700,160 700,230 L700,570 C700,640 660,680 600,690 L580,718 L210,718 L190,690 C140,680 100,640 100,570 L100,230 C100,160 140,120 202,108 Z"/>

  <g class="top-rules">
    <rect class="rule" x="352" y="90" width="96" height="3"/>
    <rect class="rule" x="307" y="101" width="190" height="4"/>
  </g>

  <g class="seal-group">
    <circle class="seal-ring" cx="400" cy="313" r="140"/>
    <circle class="seal" cx="400" cy="313" r="135"/>
    <text class="title-script" x="400" y="274" text-anchor="middle">Cold</text>
    <text class="title-line" x="400" y="333" text-anchor="middle">Brew</text>
    <text class="title-line" x="400" y="394" text-anchor="middle">Coffee</text>
  </g>

  <g class="cup-icon">
    <path class="icon-fill" d="M153,425 L222,425 L222,470 C222,478 216,483 208,483 L167,483 C159,483 153,478 153,470 Z"/>
    <path class="icon-stroke" d="M222,432 C240,430 248,440 245,452 C242,462 232,466 222,464"/>
    <rect class="icon-fill" x="127" y="488" width="120" height="9" rx="3"/>
  </g>

  <g class="takeaway-icon">
    <rect class="icon-fill" x="586" y="369" width="22" height="12" rx="2"/>
    <path class="icon-fill" d="M578,381 L656,381 L662,400 L572,400 Z"/>
    <path class="icon-stroke" d="M586,403 L648,403 L642,494 L592,494 Z"/>
    <line class="icon-stroke" x1="588" y1="430" x2="646" y2="430"/>
    <line class="icon-stroke" x1="589" y1="455" x2="645" y2="455"/>
  </g>

  <rect class="rule shelf" x="122" y="500" width="546" height="7"/>

  <path class="pattern-area" role="img" aria-label="Fine cream chevron pattern band"
        d="M122,512 L668,512 L668,560 C660,640 620,668 560,680 L240,680 C180,668 130,640 122,560 Z"/>

  <g class="bottom-rules">
    <rect class="rule" x="303" y="686" width="187" height="4"/>
    <rect class="rule" x="350" y="698" width="95" height="3"/>
  </g>
</svg>
</body>
</html>
```